ZRD Roofing Billboard Design

Looking for a fresh new billboard design with my new headshot photo and using some info from my previous billboard and maybe website for design/content inspiration. My website is https://zrdroofing.com/

Also attached are my logo and current lawn sign design. I am looking for something simple, clean and modern. The landing page website should be 3816tops.com like my previous billboard has.

```html
<!DOCTYPE html>
<html lang="en">
<head>
<meta charset="utf-8">
<title>ZRD Roofing Billboard</title>
<link href="https://fonts.googleapis.com/css2?family=Oswald:wght@600;700&family=Montserrat:wght@700;900&display=swap" rel="stylesheet">
<style>
  :root {
    --navy: #0f1f3d;
    --green: #8fa83a;
    --white: #ffffff;
    --shadow-grey: #b9bcc0;
    --sky-top: #3f7fd0;
    --sky-bottom: #a9c4e2;
    --roof: #4b5766;
    --shirt: #b9c6dc;
    --skin: #c99a80;
  }
  * { margin: 0; padding: 0; box-sizing: border-box; }
  html, body { width: 1200px; height: 350px; overflow: hidden; background: var(--white); }
  .billboard { position: relative; width: 1200px; height: 350px; background: var(--white); overflow: hidden; }
  .backdrop { position: absolute; inset: 0; width: 1200px; height: 350px; }
  .brand {
    position: absolute; left: 96px; top: 28px; width: 130px;
    display: flex; align-items: center; gap: 6px;
    font-family: "Montserrat", sans-serif; font-weight: 700; font-size: 15px; color: var(--navy);
    white-space: nowrap;
  }
  .brand-dot { width: 12px; height: 12px; border-radius: 50%; background: var(--green); flex: none; }
  .headshot {
    position: absolute; left: 0; top: 94px; width: 295px; height: 256px;
    background: linear-gradient(180deg, var(--skin) 0%, #b8a49a 45%, var(--shirt) 60%, #a9b8d0 100%);
    border-radius: 120px 120px 0 0;
  }
  .headline {
    position: absolute; left: 270px; width: 520px; text-align: center;
    font-family: "Oswald", sans-serif; font-weight: 700; text-transform: uppercase; line-height: 1;
  }
  .headline--trusted { top: 18px; font-size: 54px; color: var(--navy); }
  .headline--town { top: 64px; font-size: 54px; color: var(--green); }
  .service-title {
    position: absolute; left: 270px; width: 520px; top: 128px; text-align: center;
    font-family: "Montserrat", sans-serif; font-weight: 900; font-size: 64px; line-height: 1;
    color: var(--navy); text-transform: uppercase; letter-spacing: -1px;
  }
  .service-sub {
    position: absolute; left: 270px; width: 520px; top: 202px; text-align: center;
    font-family: "Montserrat", sans-serif; font-weight: 700; font-size: 32px; line-height: 1;
    color: var(--navy); text-transform: uppercase; letter-spacing: 6px;
  }
  .landing-url {
    position: absolute; left: 300px; width: 460px; top: 262px; text-align: center;
    font-family: "Oswald", sans-serif; font-weight: 600; font-size: 54px; line-height: 66px;
    color: var(--white); text-transform: uppercase;
  }
  .price-badge {
    position: absolute; left: 768px; top: 198px; width: 186px; height: 118px;
    border-radius: 50%; background: var(--green); border: 3px solid var(--white);
    transform: rotate(-9deg);
    font-family: "Oswald", sans-serif; font-weight: 700; color: var(--white); text-transform: uppercase;
    display: flex; flex-direction: column; align-items: center; justify-content: center; line-height: 1;
  }
  .price-badge__lead { font-size: 28px; }
  .price-badge__amount { font-size: 44px; }
  .price-badge__at { font-size: 22px; margin-right: 4px; }
</style>
</head>
<body>
  <main class="billboard">
    <svg class="backdrop" viewBox="0 0 1200 350" aria-hidden="true">
      <defs>
        <linearGradient id="sky" x1="0" y1="0" x2="0" y2="1">
          <stop offset="0" stop-color="var(--sky-top)"/>
          <stop offset="0.35" stop-color="var(--sky-bottom)"/>
          <stop offset="0.5" stop-color="var(--roof)"/>
          <stop offset="1" stop-color="#3c4756"/>
        </linearGradient>
      </defs>
      <polygon class="corner-accent" points="0,0 58,0 266,350 0,350" fill="var(--green)"/>
      <polygon class="photo-shadow" points="792,0 812,0 945,350 925,350" fill="var(--shadow-grey)"/>
      <polygon class="info-band" points="266,261 950,261 968,328 266,328" fill="var(--navy)"/>
    </svg>
    <svg class="backdrop" viewBox="0 0 1200 350" role="img" aria-label="Photo of a house roofline with grey shingles and a white dormer under a blue sky with clouds">
      <polygon points="808,0 1200,0 1200,350 935,350" fill="url(#sky)"/>
    </svg>

    <div class="brand"><span class="brand-dot"></span>ZRD Roofing</div>

    <div class="headshot" role="img" aria-label="Headshot of the company owner in a light blue shirt"></div>

    <h1 class="headline headline--trusted">Your Trusted Roofer</h1>
    <p class="headline headline--town">In Newington, CT</p>
    <h2 class="service-title">Full Roof</h2>
    <p class="service-sub">Replacements</p>
    <p class="landing-url">3816tops.com</p>

    <div class="price-badge">
      <span class="price-badge__lead">Starting</span>
      <span class="price-badge__amount"><span class="price-badge__at">at</span>$7,499</span>
    </div>
  </main>
</body>
</html>
```